Flyer for Makeup Class

A flyer for my makeup class promotion. I am a make up artist starting a group class to teach makeup to ladies. I have attached some verbiage handwritten. My picture is the one in pink hijab. I have also attached some inspiration ideas and color combination (the colors in the cake design are the ones I want to use).

Target Market(s)

Ladies looking to learn make up from a make up artist

Industry/Entity Type

Hair And Beauty

Requirements
Must have
• The verbiage / description that I have hand written should be written using graphics and nice fonts. You can change the exact wording to make it better.

```html
<!DOCTYPE html>
<html lang="en">
<head>
<meta charset="utf-8">
<title>Exclusive Makeup Master Class</title>
<link href="https://fonts.googleapis.com/css2?family=Cormorant+Unicase:wght@300;400&family=Montserrat:wght@400;500&display=swap" rel="stylesheet">
<style>
  :root {
    --flyer-pink: #cf4a8c;
    --flyer-pink-light: #dc6aa2;
    --flyer-pink-deep: #b93779;
    --ink-white: #ffffff;
    --photo-blush: #f3c9d6;
    --photo-rose: #e7a1bb;
  }
  * { margin: 0; padding: 0; box-sizing: border-box; }
  html, body { width: 849px; height: 1200px; overflow: hidden; }
  body { background: var(--flyer-pink); font-family: "Montserrat", sans-serif; color: var(--ink-white); }
  .flyer {
    position: relative; width: 849px; height: 1200px; overflow: hidden;
    background: linear-gradient(90deg, var(--flyer-pink-deep) 0%, var(--flyer-pink) 18%, var(--flyer-pink-light) 50%, var(--flyer-pink) 82%, var(--flyer-pink-deep) 100%);
  }
  .dotted-frame { position: absolute; inset: 0; }
  .ornament { position: absolute; border-radius: 50%; opacity: .35; }
  .ornament--top-left { left: 40px; top: 40px; width: 150px; height: 150px; background: radial-gradient(circle, var(--flyer-pink-light), transparent 70%); }
  .ornament--top-right { right: 40px; top: 60px; width: 160px; height: 160px; background: radial-gradient(circle, var(--flyer-pink-light), transparent 70%); }
  .ornament--bottom-right { right: 40px; bottom: 60px; width: 220px; height: 200px; background: radial-gradient(circle, var(--flyer-pink-light), transparent 70%); }
  .title {
    position: absolute; top: 70px; left: 0; right: 0; text-align: center;
    font-family: "Cormorant Unicase", serif; font-weight: 300; font-size: 64px; line-height: 1.08; letter-spacing: 1px;
  }
  .presenter { position: absolute; top: 232px; left: 0; right: 0; text-align: center; font-size: 24px; letter-spacing: .5px; }
  .presenter .by { display: block; font-size: 22px; margin-bottom: 2px; }
  .event-details { position: absolute; top: 318px; left: 0; right: 0; text-align: center; font-size: 19px; line-height: 1.35; text-transform: uppercase; }
  .audience-pill {
    position: absolute; top: 432px; left: 150px; width: 549px; height: 50px;
    border: 2px solid var(--ink-white); border-radius: 25px;
    display: flex; align-items: center; justify-content: center; font-size: 19px; font-weight: 500;
  }
  .class-perks { position: absolute; top: 518px; left: 0; right: 0; text-align: center; font-size: 19px; line-height: 1.4; }
  .portrait {
    position: absolute; left: 90px; bottom: 30px; width: 330px; height: 430px;
    background: linear-gradient(180deg, var(--photo-blush) 0%, var(--photo-rose) 70%, var(--flyer-pink-deep) 100%);
    border-radius: 160px 160px 0 0;
  }
  .booking {
    position: absolute; left: 445px; top: 790px; width: 320px; padding: 14px 18px;
    border: 2px solid var(--ink-white); border-radius: 10px;
    font-size: 18px; line-height: 1.45;
  }
  .booking-heading { font-weight: 500; text-transform: uppercase; }
</style>
</head>
<body>
<main class="flyer">
  <div class="ornament ornament--top-left" role="img" aria-label="Line-art makeup products decoration"></div>
  <div class="ornament ornament--top-right" role="img" aria-label="Line-art makeup brush decoration"></div>
  <div class="ornament ornament--bottom-right" role="img" aria-label="Line-art cosmetics and perfume decoration"></div>

  <svg class="dotted-frame" width="849" height="1200" viewBox="0 0 849 1200" aria-hidden="true">
    <rect x="28" y="28" width="793" height="1144" fill="none" stroke="#ffffff" stroke-width="6" stroke-linecap="round" stroke-dasharray="0 16"/>
  </svg>

  <h1 class="title">Exclusive Makeup<br>Master Class</h1>

  <p class="presenter"><span class="by">by</span>SANA MALIK (UK BASED MUA)</p>

  <p class="event-details">Venue: Rosewood Hall, Lakeview Road, Islamabad<br>6th April 2019<br>11:30 – 5:30 PM</p>

  <p class="audience-pill">Perfect For Professionals, Beginners And Makeup Lovers</p>

  <p class="class-perks">This Class Is Packed With Loads Of Information, Tips,<br>Live Demos, Goodie Bag, Certificate,<br>Q&amp;A, Lunch &amp; Much More...</p>

  <div class="portrait" role="img" aria-label="Portrait photo of the makeup artist wearing a pink hijab"></div>

  <div class="booking">
    <p class="booking-heading">To Book Your Place Contact</p>
    <p>07700 900 142</p>
    <p>0300 555 0198</p>
    <p>instagram @sanamalik.studio</p>
  </div>
</main>
</body>
</html>
```